Tending Our Garden eBook Cover Design

I want to deisgn a cover for my eBook (FRONT COVER) and the title is:

What I Grew From a Single Spark. And Why It Matters
By KT Dorran

TITLE CHANGED TO: UNDER THE WILLOW TREE; WHERE I FOUND MY QUIET STRENGTH AND WHERE YOU MIGHT TOO

The color palette is attached. Along with some photos options of me. Along with the ebook in WORD Document. My website is www.KTDorranLive.example. You can use a different color palette if you think it is best

Target Market(s)

women who look to build a personal brand

Industry/Entity Type

health and wellness

Requirements
Must have
• the title
Nice to have
• use my picture on the cover; but that is optional
Should not have
• any men

```html
<!DOCTYPE html>
<html lang="en">
<head>
<meta charset="utf-8">
<title>Under the Willow Tree — KT Dorran</title>
<link href="https://fonts.googleapis.com/css2?family=Lato:wght@700;900&family=Montserrat:wght@500&display=swap" rel="stylesheet">
<style>
  :root{
    --paper:#ffffff;
    --night:#0b0a0e;
    --ink-deep:#5d252b;
    --ink-soft:#8b4a52;
    --band-peach:#ecc6bb;
    --band-blush:#f6c6d5;
    --band-rose:#dfa1b1;
    --band-mauve:#b38387;
    --band-pink:#e68a9d;
    --white:#ffffff;
  }
  html,body{margin:0;padding:0;overflow:hidden;background:var(--paper);}
  .cover{position:relative;width:750px;height:1200px;background:var(--paper);overflow:hidden;}
  .cover-art{position:absolute;left:0;top:0;width:750px;height:1200px;}
  .author-name{
    position:absolute;left:37px;top:95px;width:674px;margin:0;
    text-align:center;color:var(--white);
    font-family:'Montserrat',sans-serif;font-weight:500;font-size:84px;letter-spacing:1px;line-height:1;
  }
  .title-small{font-family:'Lato',sans-serif;font-weight:700;}
  .title-big{font-family:'Lato',sans-serif;font-weight:900;}
</style>
</head>
<body>
<div class="cover">
  <svg class="cover-art" width="750" height="1200" viewBox="0 0 750 1200" aria-labelledby="book-title">
    <title id="book-title">Under the Willow Tree; Where I Found My Quiet Strength and Where You Might Too</title>
    <defs>
      <clipPath id="frame"><rect x="37" y="60" width="674" height="1079"/></clipPath>
      <radialGradient id="portrait-tone" cx="0.45" cy="0.78" r="0.6">
        <stop offset="0" stop-color="#f0281c"/>
        <stop offset="0.45" stop-color="#b5241f"/>
        <stop offset="0.75" stop-color="#2a1012"/>
        <stop offset="1" stop-color="#0b0a0e"/>
      </radialGradient>
      <linearGradient id="band-fade" x1="0" x2="1" y1="0" y2="0">
        <stop offset="0" stop-color="#fff" stop-opacity="0"/>
        <stop offset="0.75" stop-color="#fff" stop-opacity="0"/>
        <stop offset="1" stop-color="#3a1a2a" stop-opacity="0.55"/>
      </linearGradient>
    </defs>
    <g clip-path="url(#frame)">
      <rect class="portrait" x="37" y="60" width="674" height="1079" fill="url(#portrait-tone)" role="img" aria-label="Portrait photo of the author in a red dress, seated against a dark studio backdrop"/>
      <polygon class="band band-peach" points="37,732 711,617 711,682 37,797" fill="var(--band-peach)" opacity="0.92"/>
      <polygon class="band band-blush" points="37,797 711,682 711,782 37,897" fill="var(--band-blush)" opacity="0.95"/>
      <polygon class="band band-rose" points="37,897 711,782 711,842 37,957" fill="var(--band-rose)" opacity="0.92"/>
      <polygon class="band band-mauve" points="37,957 711,842 711,897 37,1012" fill="var(--band-mauve)" opacity="0.95"/>
      <polygon class="band band-pink" points="37,1012 711,897 711,1015 37,1130" fill="var(--band-pink)" opacity="0.95"/>
      <polygon class="band-shade" points="37,732 711,617 711,1015 37,1130" fill="url(#band-fade)"/>
    </g>
    <g class="title">
      <text class="title-small" x="82" y="772" font-size="40" fill="var(--ink-soft)" transform="rotate(-14 82 772)">Under the</text>
      <text class="title-big" x="112" y="868" font-size="86" fill="var(--ink-deep)" transform="rotate(-14 112 868)">Willow Tree;</text>
      <text class="title-small" x="232" y="918" font-size="27" fill="var(--ink-soft)" transform="rotate(-14 232 918)">Where I Found My Quiet Strength</text>
      <text class="title-small" x="118" y="984" font-size="38" fill="var(--white)" transform="rotate(-14 118 984)">And Where</text>
      <text class="title-big" x="68" y="1098" font-size="98" fill="var(--white)" transform="rotate(-14 68 1098)">You Might<tspan class="title-small" font-size="38" dx="10">Too</tspan></text>
    </g>
  </svg>
  <h1 class="author-name">KT Dorran</h1>
</div>
</body>
</html>
```